Website design for new health & wellness company

We need our website to be designed in a user friendly way. Needs to be aesthetically pleasing to viewer and easy to navigate and upload content for our small team . The logo should be completely redesigned , please do not reference the current one thats on our site for a starting place. (included below though) We want to move away from that.

the website is : www.brightpathforward.com

We are a small group of writers/coaches who believe that to change the world you have to be the change and we provide tips/suggestions for every day life that if followed can make a huge difference in your life and overall being.

Target Market(s)

Men and women ages 22 to 50

Industry/Entity Type

Health And Wellness

Logo Text

Cultivate the life of your dreams

Coding

Coded - Design and coding required

Number of Pages Required

3 page

Font styles to use
Sans Serif

Colors

Designer to choose colors to be used in the design.

Requirements
Must have
• Easy to navigate. Mobile friendly. Gender neutral, should appeal to both.

```html
<!DOCTYPE html>
<html lang="en">
<head>
<meta charset="utf-8">
<title>Bright Path Forward — Health &amp; Wellness</title>
<link rel="stylesheet" href="https://fonts.googleapis.com/css2?family=Lato:wght@400;700;900&display=swap">
<style>
:root{
  --navy:#24466b;
  --navy-dark:#1c3957;
  --ink:#1e1e1e;
  --muted:#555;
  --rule:#dcdcdc;
  --footer-bg:#ebebec;
  --white:#fff;
}
*{box-sizing:border-box;margin:0;padding:0}
html,body{width:1200px;height:3416px;overflow:hidden}
body{font-family:"Lato",Arial,sans-serif;color:var(--ink);background:var(--white);position:relative}
.abs{position:absolute}
a{color:inherit;text-decoration:none}

/* header */
.site-header{top:0;left:0;width:1200px;height:82px;background:var(--white)}
.brand{display:flex;align-items:center;gap:10px;width:200px}
.brand-dot{width:38px;height:38px;border-radius:50%;background:var(--navy);flex:none}
.brand-name{font-weight:900;font-size:18px;color:var(--navy);letter-spacing:.5px;line-height:1.1}
.main-nav{left:402px;top:28px;display:flex}
.main-nav a{font-size:12px;font-weight:700;padding:8px 14px;letter-spacing:.3px;margin-right:14px}
.main-nav a.active{background:var(--navy);color:var(--white)}
.search{left:929px;top:27px;width:137px;height:33px;border:1px solid #9a9a9a;display:flex;align-items:center;justify-content:space-between;padding:0 10px;font-size:10px;letter-spacing:.5px;color:#444}

/* hero */
.hero{top:82px;left:0;width:1200px;height:392px;background:linear-gradient(100deg,#7d8a4a 0%,#b7a86a 35%,#d8d2b4 55%,#9aa15e 80%,#6a7a3c 100%)}
.hero-title{left:210px;top:128px;font-size:48px;font-weight:700;color:var(--white)}
.hero-sub{left:210px;top:196px;font-size:19px;font-weight:700;color:var(--white)}
.dots{left:549px;top:330px;display:flex;gap:12px}
.dots span{width:10px;height:10px;border-radius:50%;background:var(--white)}
.dots span.off{background:transparent;border:2px solid var(--white)}

/* labels */
.section-label{left:132px;width:184px;height:44px;background:var(--navy);color:var(--white);font-size:15px;font-weight:700;display:flex;align-items:center;padding-left:18px;letter-spacing:.3px}
.section-label.short{width:104px}
.section-label.mid{width:116px}

/* latest */
.feature-card{left:132px;top:597px;width:412px;height:432px;border:1px solid var(--rule)}
.feature-img{height:275px;background:linear-gradient(180deg,#8fb4d4 0%,#b8c9cf 50%,#c9a470 100%)}
.feature-body{padding:20px 24px}
.meta{font-size:10px;color:#333}
.meta .sep{margin:0 6px}
.feature-title{font-size:15px;font-weight:700;margin:8px 0 12px}
.feature-text{font-size:12px;line-height:1.55;color:var(--muted)}
.mini{display:flex;gap:14px;width:240px}
.mini-thumb{width:80px;height:68px;flex:none}
.mini .meta{font-size:9px;margin-top:4px}
.mini-title{font-size:11.5px;font-weight:700;line-height:1.5;margin-top:6px;width:100px}

/* grid */
.tile{width:298px}
.tile-img{height:241px}
.tile .meta{margin-top:26px}
.tile-title{font-size:17px;font-weight:400;line-height:28px;margin-top:8px;text-transform:uppercase}

/* popular */
.arrows{left:1018px;top:2444px;display:flex;gap:14px}
.pop-card{top:2498px;width:221px;height:328px;border:1px solid var(--rule);padding:7px}
.pop-img{height:155px}
.pop-card .meta{margin:16px 8px 0}
.pop-title{font-size:14px;font-weight:700;margin:12px 8px 0;line-height:1.4}
.pop-text{font-size:11.5px;color:var(--muted);line-height:1.5;margin:12px 8px 0}

/* footer */
.site-footer{top:2887px;left:0;width:1200px;height:529px;background:var(--footer-bg)}
.follow-title{left:102px;top:3082px;width:220px;text-align:center;font-size:11px;font-weight:700;color:var(--navy)}
.social{left:136px;display:flex;align-items:center;gap:12px;font-size:12px}
.social i{width:24px;height:24px;border-radius:50%;display:block}
.foot-head{font-size:15px;font-weight:700;color:var(--navy);top:2963px}
.recent{left:394px;display:flex;gap:16px;align-items:center}
.recent-thumb{width:107px;height:57px}
.recent-title{font-size:13px;font-weight:700}
.recent-text{font-size:11.5px;color:var(--muted);margin-top:4px}
.about p{font-size:11.5px;line-height:1.6;color:var(--muted);text-align:justify;margin-bottom:20px}
.read-more{background:var(--navy);color:var(--white);font-size:10px;font-weight:700;padding:6px 12px;display:inline-block}
.foot-rule{left:132px;top:3329px;width:936px;height:1px;background:#d2d2d2}
.copyright{left:0;top:3366px;width:1200px;text-align:center;font-size:10px;color:#555}
</style>
</head>
<body>

<header class="site-header abs">
  <div class="brand abs" style="left:132px;top:20px"><span class="brand-dot"></span><span class="brand-name">BRIGHT PATH<br>FORWARD</span></div>
  <nav class="main-nav abs">
    <a class="active" href="#">HOME</a><a href="#">PLATE</a><a href="#">BRAIN</a><a href="#">BODY</a><a href="#">CONTACT US</a>
  </nav>
  <div class="search abs"><span>SEARCH</span>
    <svg width="12" height="12" viewBox="0 0 12 12"><circle cx="5" cy="5" r="3.8" fill="none" stroke="#333" stroke-width="1.5"/><line x1="8" y1="8" x2="11" y2="11" stroke="#333" stroke-width="1.6"/></svg>
  </div>
</header>

<section class="hero abs" role="img" aria-label="Runner on a sunlit country path between green fields">
  <h1 class="hero-title abs">Health &amp; Wellness</h1>
  <p class="hero-sub abs">Lorem Ipsum is simply dummy text</p>
  <div class="dots abs"><span></span><span class="off"></span><span></span><span></span><span></span></div>
</section>

<h2 class="section-label abs" style="top:519px">THE LATEST POSTS</h2>

<article class="feature-card abs">
  <div class="feature-img" role="img" aria-label="Woman with raised arms in tall grass by the sea"></div>
  <div class="feature-body">
    <p class="meta">June 05, 2017<span class="sep">|</span>3 Comments</p>
    <h3 class="feature-title">There are many variations of passages</h3>
    <p class="feature-text">There are many variations of passages of Lorem Ipsum available, but the majority have suffered alteration in some form, by injected humour, or randomise</p>
  </div>
</article>

<div class="mini abs" style="left:560px;top:597px"><div class="mini-thumb" role="img" aria-label="Yoga at sunset" style="background:linear-gradient(#e9a545,#7a4a1c)"></div><div><p class="meta">March 17, 2017</p><p class="mini-title">Lorem Ipsum is simply dum</p></div></div>
<div class="mini abs" style="left:560px;top:688px"><div class="mini-thumb" role="img" aria-label="Hands holding a small plant" style="background:linear-gradient(#2d4a6a,#8b6b55)"></div><div><p class="meta">March 17, 2017</p><p class="mini-title">Lorem Ipsum is simply dummy</p></div></div>
<div class="mini abs" style="left:560px;top:779px"><div class="mini-thumb" role="img" aria-label="Workout in a gym" style="background:linear-gradient(#c9c2bb,#7b5a4a)"></div><div><p class="meta">March 17, 2017</p><p class="mini-title">Lorem Ipsum is simply dummy</p></div></div>
<div class="mini abs" style="left:560px;top:868px"><div class="mini-thumb" role="img" aria-label="Stretching outdoors" style="background:linear-gradient(#b6c58a,#d9c8a5)"></div><div><p class="meta">March 17, 2017</p><p class="mini-title">Lorem Ipsum is simply dummy</p></div></div>
<div class="mini abs" style="left:560px;top:959px"><div class="mini-thumb" role="img" aria-label="Couple relaxing together" style="background:linear-gradient(#a08a78,#5e4a3e)"></div><div><p class="meta">March 17, 2017</p><p class="mini-title">Lorem Ipsum is simply dummy</p></div></div>

<div class="mini abs" style="left:783px;top:583px"><div class="mini-thumb" role="img" aria-label="Meditation at sunrise" style="background:linear-gradient(#f0b640,#c7782a)"></div><div><p class="meta">June 06, 2017</p><p class="mini-title">Lorem Ipsum is simply dum</p></div></div>
<div class="mini abs" style="left:783px;top:679px"><div class="mini-thumb" role="img" aria-label="Red heart in open hands" style="background:linear-gradient(#e8e2e0,#c9a8a6)"></div><div><p class="meta">June 06, 2017</p><p class="mini-title">Lorem Ipsum is simply dum</p></div></div>
<div class="mini abs" style="left:783px;top:771px"><div class="mini-thumb" role="img" aria-label="Red family paper cutout" style="background:linear-gradient(#b4302c,#6e1f1c)"></div><div><p class="meta">June 06, 2017</p><p class="mini-title">Lorem Ipsum is simply dum</p></div></div>
<div class="mini abs" style="left:783px;top:863px"><div class="mini-thumb" role="img" aria-label="Portrait in dim light" style="background:linear-gradient(#6a6a6a,#2e2e2e)"></div><div><p class="meta">June 06, 2017</p><p class="mini-title">Lorem Ipsum is simply dum</p></div></div>
<div class="mini abs" style="left:783px;top:957px"><div class="mini-thumb" role="img" aria-label="Child jumping on green grass" style="background:linear-gradient(#7aa83c,#3f7a24)"></div><div><p class="meta">June 06, 2017</p><p class="mini-title">Lorem Ipsum is simply dum</p></div></div>

<h2 class="section-label short abs" style="top:1079px">PLATE</h2>
<article class="tile abs" style="left:132px;top:1157px"><div class="tile-img" role="img" aria-label="Festive plate with vegetables on a yellow table" style="background:linear-gradient(135deg,#e8c23a,#c85a30 60%,#8a3a22)"></div><p class="meta">June 05, 2017<span class="sep">|</span>3 Comments</p><h3 class="tile-title">There are many variati<br>ons of passages</h3></article>
<article class="tile abs" style="left:451px;top:1157px"><div class="tile-img" role="img" aria-label="Plate with flatbread and blossoms on blue" style="background:linear-gradient(135deg,#8fb1cc,#d9cbb6 55%,#a9c1d3)"></div><p class="meta">June 05, 2017<span class="sep">|</span>3 Comments</p><h3 class="tile-title">There are many variati<br>ons of passages</h3></article>
<article class="tile abs" style="left:770px;top:1157px"><div class="tile-img" role="img" aria-label="Colourful ceramic plates seen from above" style="background:linear-gradient(135deg,#c94a38,#e8d7b4 40%,#3a7f8a 70%,#d4a32c)"></div><p class="meta">June 05, 2017<span class="sep">|</span>3 Comments</p><h3 class="tile-title">There are many variati<br>ons of passages</h3></article>

<h2 class="section-label short abs" style="top:1535px">BODY</h2>
<article class="tile abs" style="left:132px;top:1605px"><div class="tile-img" role="img" aria-label="Measuring tape around a waist" style="background:linear-gradient(135deg,#2f9aa8,#a6b08a 55%,#2b8893)"></div><p class="meta">June 05, 2017<span class="sep">|</span>3 Comments</p><h3 class="tile-title">There are many variati<br>ons of passages</h3></article>
<article class="tile abs" style="left:451px;top:1605px"><div class="tile-img" role="img" aria-label="Hands on a bare midriff" style="background:linear-gradient(180deg,#eae6e3,#c58a6a 60%,#a86a4c)"></div><p class="meta">June 05, 2017<span class="sep">|</span>3 Comments</p><h3 class="tile-title">There are many variati<br>ons of passages</h3></article>
<article class="tile abs" style="left:770px;top:1605px"><div class="tile-img" role="img" aria-label="Smiling woman with towel in a green park" style="background:linear-gradient(135deg,#3e7a34,#c9b08a 55%,#4c8a3a)"></div><p class="meta">June 05, 2017<span class="sep">|</span>3 Comments</p><h3 class="tile-title">There are many variati<br>ons of passages</h3></article>

<h2 class="section-label short abs" style="top:1981px">BRAIN</h2>
<article class="tile abs" style="left:132px;top:2056px"><div class="tile-img" role="img" aria-label="Glowing brain inside a head silhouette" style="background:radial-gradient(circle at 50% 40%,#6a7e96,#1a2029 65%)"></div><p class="meta">June 05, 2017<span class="sep">|</span>3 Comments</p><h3 class="tile-title">There are many variati<br>ons of passages</h3></article>
<article class="tile abs" style="left:451px;top:2056px"><div class="tile-img" role="img" aria-label="Blue digital brain on a grid" style="background:radial-gradient(circle at 50% 45%,#3fb6f0,#0c3b6a 55%,#061a30)"></div><p class="meta">June 05, 2017<span class="sep">|</span>3 Comments</p><h3 class="tile-title">There are many variati<br>ons of passages</h3></article>
<article class="tile abs" style="left:770px;top:2056px"><div class="tile-img" role="img" aria-label="Glowing brain held in a hand" style="background:radial-gradient(circle at 50% 35%,#e8d4b0,#5a4a3a 40%,#151515 75%)"></div><p class="meta">June 05, 2017<span class="sep">|</span>3 Comments</p><h3 class="tile-title">There are many variati<br>ons of passages</h3></article>

<h2 class="section-label mid abs" style="top:2436px">POPULAR</h2>
<div class="arrows abs">
  <svg width="16" height="24" viewBox="0 0 16 24"><polyline points="12,3 4,12 12,21" fill="none" stroke="#666" stroke-width="2"/></svg>
  <svg width="16" height="24" viewBox="0 0 16 24"><polyline points="4,3 12,12 4,21" fill="none" stroke="#666" stroke-width="2"/></svg>
</div>
<article class="pop-card abs" style="left:132px"><div class="pop-img" role="img" aria-label="Red heart with a stethoscope" style="background:linear-gradient(135deg,#e9e4e0,#c43a3a 50%,#3a7a8a)"></div><p class="meta">June 05, 2017</p><h3 class="pop-title">There are many variations of passages</h3><p class="pop-text">It uses a dictionary of over 200 Latin words, combined with a handful of model.</p></article>
<article class="pop-card abs" style="left:369px"><div class="pop-img" role="img" aria-label="Thumbs up on a dark background" style="background:linear-gradient(135deg,#1f3848,#c79a7a 55%,#1f3848)"></div><p class="meta">June 05, 2017</p><h3 class="pop-title">There are many variations of passages</h3><p class="pop-text">It uses a dictionary of over 200 Latin words, combined with a handful of model.</p></article>
<article class="pop-card abs" style="left:606px"><div class="pop-img" role="img" aria-label="Man resting on a bright sofa" style="background:linear-gradient(135deg,#f0f2f4,#9fb3c6 55%,#3a6a9a)"></div><p class="meta">June 05, 2017</p><h3 class="pop-title">There are many variations of passages</h3><p class="pop-text">It uses a dictionary of over 200 Latin words, combined with a handful of model.</p></article>
<article class="pop-card abs" style="left:843px"><div class="pop-img" role="img" aria-label="Runner's feet on a road at sunset" style="background:linear-gradient(135deg,#e8b07a,#a8503a 55%,#3a2a22)"></div><p class="meta">June 05, 2017</p><h3 class="pop-title">There are many variations of passages</h3><p class="pop-text">It uses a dictionary of over 200 Latin words, combined with a handful of model.</p></article>

<footer class="site-footer abs"></footer>
<div class="brand abs" style="left:102px;top:2956px"><span class="brand-dot"></span><span class="brand-name">BRIGHT PATH<br>FORWARD</span></div>
<p class="follow-title abs">FOLLOW US</p>
<p class="social abs" style="top:3123px"><i style="background:#3b5998"></i>Like us on Circlet</p>
<p class="social abs" style="top:3162px"><i style="background:#2a9fd8"></i>Follow us on Chirper</p>
<p class="social abs" style="top:3201px"><i style="background:#d34836"></i>Follow us on Plusly</p>
<p class="social abs" style="top:3240px"><i style="background:#3a5a9a"></i>Follow us on Linkwork</p>

<h4 class="foot-head abs" style="left:394px">RECENT POSTS</h4>
<div class="recent abs" style="top:3008px"><div class="recent-thumb" role="img" aria-label="Fresh fruit bowl" style="background:linear-gradient(135deg,#c64a6a,#6aa04a)"></div><div><p class="recent-title">There are many variations</p><p class="recent-text">It uses a dictionary of over</p></div></div>
<div class="recent abs" style="top:3076px"><div class="recent-thumb" role="img" aria-label="Green leafy garden" style="background:linear-gradient(135deg,#4e8a2a,#a4c060)"></div><div><p class="recent-title">It is a long established fact</p><p class="recent-text">It uses a dictionary of over</p></div></div>
<div class="recent abs" style="top:3145px"><div class="recent-thumb" role="img" aria-label="Person relaxing indoors" style="background:linear-gradient(135deg,#c8a07a,#6a4a3a)"></div><div><p class="recent-title">Lorem Ipsum text</p><p class="recent-text">It uses a dictionary of over</p></div></div>
<div class="recent abs" style="top:3213px"><div class="recent-thumb" role="img" aria-label="Hands forming a heart at sunset" style="background:linear-gradient(135deg,#f0c47a,#d8884a)"></div><div><p class="recent-title">Contrary to popular belie</p><p class="recent-text">It uses a dictionary of over</p></div></div>

<h4 class="foot-head abs" style="left:770px">ABOUT BRIGHT PATH FORWARD</h4>
<div class="about abs" style="left:770px;top:3005px;width:296px">
  <p>There are many variations of passages of Lorem Ipsum available, but the majority have suffered alteration in some form, by injected humour, or randomised words which don't look even slightly believable.</p>
  <p>It is a long established fact that a reader will be distracted by the readable content of a page when looking at its layout. The point of using Lorem Ipsum is that it has a more-or-less normal distribution of letters, as opposed.</p>
  <a class="read-more" href="#">READ MORE</a>
</div>

<div class="foot-rule abs"></div>
<p class="copyright abs">Copyrights @ 2017 All Rights Reserved</p>

</body>
</html>
```